"The Quillvanes"(Entertainment) needs a classy modern CD cover design

"The Quillvanes", a vocal trio that does Soul Motown and Swing music needs a classy dynamic and modern design for their first album.
We have a photo that needs enhancing and a background. We are open to any ideas as long as the design is innovative and creative.
The title of the album is "Velvet Lanterns". The focus should be on the performers and the movement and energy of the photo should be kept.
We may commission the successful designer for the rest of the album.

Industry/Entity Type

Entertainment

Requirements
Must have
• The name of the group, "The Quillvanes"
• and the title of the album, "Velvet Lanterns"
• Colour

```html
<!DOCTYPE html>
<html lang="en">
<head>
<meta charset="utf-8">
<title>The Quillvanes – Velvet Lanterns CD Label</title>
<link rel="stylesheet" href="https://fonts.googleapis.com/css2?family=Poiret+One&display=swap">
<style>
  :root {
    --paper: #ffffff;
    --ink: #0a0a0b;
    --frame: #1a1a1a;
    --title-violet: #c455dc;
    --name-lime: #dbe977;
    --streak-violet: #9b2fc8;
    --streak-orchid: #c85ae6;
    --streak-lemon: #ece35c;
    --streak-aqua: #62dcd2;
    --stage-red: #d63a22;
    --stage-silver: #b9b9bd;
  }
  * { margin: 0; padding: 0; box-sizing: border-box; }
  html, body {
    width: 1200px;
    height: 901px;
    overflow: hidden;
    background: var(--paper);
  }
  .cd-sheet {
    position: relative;
    width: 1200px;
    height: 901px;
    background: var(--paper);
  }
  .cd-sheet__art {
    position: absolute;
    inset: 0;
    display: block;
  }
  .band-name {
    position: absolute;
    top: 60px;
    left: 0;
    width: 1200px;
    text-align: center;
    font-family: "Poiret One", sans-serif;
    font-size: 23px;
    letter-spacing: 1px;
    color: var(--name-lime);
  }
  .album-title {
    position: absolute;
    font-family: "Poiret One", sans-serif;
    font-weight: 400;
    color: var(--title-violet);
    font-size: 80px;
    line-height: 1;
    letter-spacing: -1px;
  }
  .album-title__line { position: absolute; white-space: nowrap; }
  .album-title__line--first { left: 312px; top: 143px; }
  .album-title__line--second { left: 460px; top: 203px; }
</style>
</head>
<body>
<main class="cd-sheet">
  <svg class="cd-sheet__art" viewBox="0 0 1200 901" width="1200" height="901">
    <defs>
      <clipPath id="disc-clip">
        <circle cx="601" cy="450" r="450"/>
      </clipPath>
      <linearGradient id="light-streaks" x1="0" y1="0" x2="1" y2="0.2">
        <stop offset="0" stop-color="var(--streak-violet)"/>
        <stop offset="0.08" stop-color="var(--streak-lemon)"/>
        <stop offset="0.2" stop-color="var(--streak-orchid)"/>
        <stop offset="0.5" stop-color="var(--streak-violet)"/>
        <stop offset="0.66" stop-color="var(--streak-aqua)"/>
        <stop offset="0.78" stop-color="var(--streak-lemon)"/>
        <stop offset="0.9" stop-color="var(--streak-orchid)"/>
        <stop offset="1" stop-color="#2a0a35"/>
      </linearGradient>
      <linearGradient id="stage-tones" x1="0" y1="0" x2="0" y2="1">
        <stop offset="0" stop-color="var(--stage-red)" stop-opacity="0"/>
        <stop offset="0.12" stop-color="var(--stage-red)" stop-opacity="0.8"/>
        <stop offset="0.4" stop-color="var(--stage-silver)" stop-opacity="0.75"/>
        <stop offset="0.75" stop-color="var(--ink)" stop-opacity="0.9"/>
        <stop offset="1" stop-color="var(--ink)"/>
      </linearGradient>
    </defs>

    <rect class="sheet-frame" x="1.5" y="1.5" width="1197" height="897" fill="none" stroke="var(--frame)" stroke-width="1.5"/>

    <g class="disc" clip-path="url(#disc-clip)">
      <rect x="140" y="0" width="925" height="901" fill="var(--ink)"/>
      <path class="disc__streaks" role="img" aria-label="Sweeping bands of violet, lemon and aqua light streaks"
            d="M130,330 C350,390 520,440 620,330 C720,230 880,225 1100,240 L1100,901 L130,901 Z"
            fill="url(#light-streaks)"/>
      <path class="disc__performers" role="img" aria-label="Photo of the three performers in bowler hats, red shirts and sequin waistcoats dancing"
            d="M200,700 C300,670 380,640 420,600 C470,585 520,565 570,560 C630,556 700,585 760,575 C840,595 930,605 1060,590 L1080,901 L180,901 Z"
            fill="url(#stage-tones)"/>
    </g>

    <circle class="disc__edge" cx="601" cy="450" r="450" fill="none" stroke="var(--frame)" stroke-width="1.5"/>
    <circle class="disc__hole" cx="602" cy="451" r="104" fill="var(--paper)" stroke="var(--frame)" stroke-width="1.5"/>
  </svg>

  <p class="band-name">The Quillvanes</p>
  <h1 class="album-title">
    <span class="album-title__line album-title__line--first">Velvet</span>
    <span class="album-title__line album-title__line--second">Lanterns</span>
  </h1>
</main>
</body>
</html>
```